plumbing & gas fitting business card design

We need a business card design for a plumbing & gas fitting company. The company covers commercial, domestic and maintenance work. We would like a modern design communicating efficiency and sophistication. preferred colours would include (red grey & black) or (green grey & black). Please DO NOT include any water droplets.

Industry/Entity Type

Business

Contact Information for Business Card

Vortig Plumbing & Gas, Commercial Domestic & Maintenance, licence no. 617394K, ABN 47215830962, Phone 0417382956, Email vortigplumbingandgas@corvanet.com

```html
<!DOCTYPE html>
<html lang="en">
<head>
<meta charset="utf-8">
<title>Vortig Plumbing &amp; Gas – Business Card</title>
<link rel="stylesheet" href="https://fonts.googleapis.com/css2?family=Arimo:wght@400;700&display=swap">
<style>
  :root {
    --granite-black: #141414;
    --granite-red: #5a1414;
    --basin-grey-dark: #9a9a9a;
    --basin-grey: #c9c9c9;
    --basin-grey-light: #ececec;
    --tap-white: #ffffff;
    --brand-red: #a8161b;
    --ink: #111111;
  }
  html, body {
    margin: 0;
    padding: 0;
    width: 1200px;
    height: 694px;
    overflow: hidden;
    background: #ffffff;
  }
  .card {
    position: relative;
    width: 1200px;
    height: 694px;
    overflow: hidden;
    font-family: "Arimo", Arial, sans-serif;
    color: var(--ink);
  }
  .card__photo {
    position: absolute;
    inset: 0;
    width: 100%;
    height: 100%;
  }
  .card__details {
    position: absolute;
    left: 79px;
    top: 398px;
  }
  .company-name,
  .services {
    margin: 0;
    font-size: 34px;
    font-weight: 700;
    line-height: 46px;
  }
  .company-name {
    color: var(--brand-red);
  }
  .registration {
    margin: 0 0 16px;
    font-size: 26px;
    font-weight: 400;
    line-height: 32px;
  }
  .contact-line {
    margin: 0;
    font-size: 31px;
    font-weight: 400;
    line-height: 46px;
  }
</style>
</head>
<body>
  <main class="card">
    <svg class="card__photo" viewBox="0 0 1200 694" role="img" aria-label="Close-up photograph of a white cross-handle hot tap on a basin against a dark granite benchtop">
      <defs>
        <linearGradient id="basin-tone" x1="0" y1="0" x2="1" y2="1">
          <stop offset="0" stop-color="var(--basin-grey-dark)"/>
          <stop offset="0.45" stop-color="var(--basin-grey)"/>
          <stop offset="1" stop-color="var(--basin-grey-light)"/>
        </linearGradient>
        <radialGradient id="granite-tone" cx="0.15" cy="0.1" r="0.55">
          <stop offset="0" stop-color="var(--granite-red)"/>
          <stop offset="1" stop-color="var(--granite-black)"/>
        </radialGradient>
        <radialGradient id="tap-glow" cx="0.82" cy="0.4" r="0.3">
          <stop offset="0" stop-color="var(--tap-white)"/>
          <stop offset="1" stop-color="var(--tap-white)" stop-opacity="0"/>
        </radialGradient>
      </defs>
      <rect width="1200" height="694" fill="url(#basin-tone)"/>
      <path d="M0 0 H1200 V20 C900 40 500 60 250 200 C120 270 40 330 0 360 Z" fill="url(#granite-tone)"/>
      <rect width="1200" height="694" fill="url(#tap-glow)"/>
    </svg>

    <section class="card__details">
      <h1 class="company-name">Vortig Plumbing &amp; Gas</h1>
      <p class="services">Commercial Domestic &amp; Maintenance</p>
      <p class="registration">licence no. 617394K, ABN 47215830962</p>
      <p class="contact-line">P: 0417 382 956</p>
      <p class="contact-line">E: vortigplumbingandgas@corvanet.com</p>
    </section>
  </main>
</body>
</html>
```